Business Card Design

I need a business card design for my new solo law practice. I practice consumer bankruptcy law.

I would like a simple, functional business card that looks professional but will also be understandable to regular people - not just other lawyers.
Updates

I added a couple of possible logos that can be incorporated

I'm sorry about the confusion, but the suite number for my new office is suite #150. Thanks for your patience

Target Market(s)

the real target market is potential clients

Industry/Entity Type

Business

Contact Information for Business Card

Law Offices of Theodore M. Vance
Theodore M. Vance
Attorney at Law
Bankruptcy Law
418 Marlowe Court #210
Harlow Springs, VT 05842
(555) 317-6482 (Phone)
(555) 317-6497 (Fax)
theov@cedarpointdebtrelief.example
cedarpointdebtrelief.example

Font styles to use
Serif

Requirements
Nice to have
• I've added some possible logos to possible incorporate

```html
<!DOCTYPE html>
<html lang="en">
<head>
<meta charset="utf-8">
<title>Theodore M. Vance – Business Card</title>
<link rel="stylesheet" href="https://fonts.googleapis.com/css2?family=Montserrat:wght@500&family=Open+Sans:wght@400&family=Cabin:wght@500&display=swap">
<style>
  :root {
    --backdrop-light: #eef0f2;
    --backdrop-dark: #c9cdd2;
    --card-white: #ffffff;
    --card-navy: #283150;
    --card-red: #7a1c16;
    --mark-green: #9cbf55;
    --ink-dark: #1f2433;
    --ink-light: #ffffff;
  }
  html, body {
    margin: 0;
    width: 1200px;
    height: 800px;
    overflow: hidden;
  }
  body {
    background: radial-gradient(ellipse at 40% 35%, var(--backdrop-light), var(--backdrop-dark));
  }
  .business-card {
    position: absolute;
    left: 160px;
    top: 151px;
    width: 880px;
    height: 498px;
    box-shadow: 0 10px 30px rgba(0,0,0,0.18);
  }
  .firm-name {
    font-family: "Cabin", sans-serif;
    font-weight: 500;
    font-size: 14px;
    fill: var(--ink-dark);
  }
  .attorney-name {
    font-family: "Montserrat", sans-serif;
    font-weight: 500;
    font-size: 18.5px;
    fill: var(--ink-light);
  }
  .attorney-title,
  .contact-line {
    font-family: "Open Sans", sans-serif;
    font-weight: 400;
    fill: var(--ink-light);
  }
  .attorney-title { font-size: 13px; }
  .contact-line { font-size: 13px; }
  .contact-icon { fill: var(--ink-light); }
  .contact-icon-stroke { fill: none; stroke: var(--ink-light); stroke-width: 1.2; }
</style>
</head>
<body>
<svg class="business-card" viewBox="0 0 542 307" xmlns="http://www.w3.org/2000/svg">
  <!-- card surfaces -->
  <rect class="card-base" x="0" y="0" width="542" height="307" fill="var(--card-white)"/>
  <rect class="card-info-panel" x="228" y="0" width="314" height="307" fill="var(--card-navy)"/>
  <rect class="card-red-tab" x="0" y="66" width="24" height="184" fill="var(--card-red)"/>
  <rect class="card-center-tab" x="18" y="66" width="230" height="184" rx="14" fill="var(--card-white)"/>

  <!-- firm name with plain circle -->
  <circle class="firm-mark-circle" cx="130" cy="133" r="52" fill="var(--mark-green)"/>
  <text class="firm-name" x="132" y="222" text-anchor="middle">Law Offices of Theodore M. Vance</text>

  <!-- attorney -->
  <text class="attorney-name" x="267" y="63">Theodore M. Vance</text>
  <text class="attorney-title" x="267" y="86">Attorney at Law Bankruptcy Law</text>

  <!-- phone -->
  <rect class="contact-icon-stroke" x="269" y="122" width="6" height="11" rx="1"/>
  <rect class="contact-icon" x="270.5" y="124" width="3" height="4"/>
  <text class="contact-line" x="297" y="132">(555) 317-6482</text>

  <!-- fax -->
  <rect class="contact-icon-stroke" x="269.5" y="151" width="7" height="4"/>
  <rect class="contact-icon" x="267" y="155" width="12" height="6" rx="1"/>
  <text class="contact-line" x="297" y="160">(555) 317-6497</text>

  <!-- email -->
  <rect class="contact-icon-stroke" x="267" y="180" width="12" height="8"/>
  <path class="contact-icon-stroke" d="M267 180 L273 185 L279 180"/>
  <text class="contact-line" x="297" y="188">theov@cedarpointdebtrelief.example</text>

  <!-- web -->
  <circle class="contact-icon-stroke" cx="273" cy="209" r="5.5"/>
  <path class="contact-icon-stroke" d="M267.5 209 H278.5 M273 203.5 C270 206 270 212 273 214.5 C276 212 276 206 273 203.5"/>
  <text class="contact-line" x="297" y="214">www.cedarpointdebtrelief.example</text>

  <!-- address -->
  <path class="contact-icon" d="M273 248 C269 242 268 240 268 237 A5 5 0 0 1 278 237 C278 240 277 242 273 248 Z"/>
  <circle cx="273" cy="237" r="1.8" fill="var(--card-navy)"/>
  <text class="contact-line" x="297" y="241">418 Marlowe Court #210</text>
  <text class="contact-line" x="297" y="261">Harlow Springs, VT 05842</text>
</svg>
</body>
</html>
```